Brennok Sports Pub. Where the locals go!!

We are creating a sports pub. We are needing a fun website that offers our menu along with an event page and general info. We have some attached links that we really like:
https://www.holvertons.com/
https://www.bistromeluna.com/
https://www.quillspardx.com/
We are doing a pirate theme but that is because the area we are in. We would like to see a pirate like in our logo doing something like drinking real time similar to the holvertons website above.
Target Market(s)
Sports Fans
Industry/Entity Type
Pub, Bar, Restaurant
Coding
Coded - Design and coding required
Number of Pages Required
3 page

```html
<!DOCTYPE html>
<html lang="en">
<head>
<meta charset="utf-8">
<title>Brennok Sports Pub</title>
<link href="https://fonts.googleapis.com/css2?family=Bebas+Neue&family=Poppins:ital,wght@0,400;0,500;0,600;1,400&display=swap" rel="stylesheet">
<style>
:root{
  --amber:#c9862f;
  --amber-light:#e2b37a;
  --brown:#2e2015;
  --brown-deep:#1e1712;
  --ink:#1b1b1b;
  --text:#6b6b6b;
  --white:#fff;
  --footer:#1d1a18;
  --sketch:rgba(120,120,120,.10);
}
*{margin:0;padding:0;box-sizing:border-box}
html,body{width:1200px;height:4894px;overflow:hidden}
body{position:relative;background:var(--white);font-family:'Poppins',sans-serif;color:var(--ink)}
.abs{position:absolute}
.display{font-family:'Bebas Neue',sans-serif;font-weight:400;letter-spacing:.5px}
.btn{position:absolute;display:flex;align-items:center;justify-content:center;background:var(--amber);color:var(--white);font-size:14px;font-weight:600;border-radius:20px;text-transform:uppercase}
.media{position:absolute;overflow:hidden}
.sketch{position:absolute;background:radial-gradient(ellipse at center,var(--sketch) 0%,rgba(120,120,120,.04) 55%,rgba(255,255,255,0) 72%)}

/* nav */
.nav{position:absolute;left:0;top:0;width:1200px;height:67px;background:var(--white)}
.nav a{position:absolute;top:25px;font-size:14px;font-weight:500;color:var(--ink);text-decoration:none;white-space:nowrap}
.brand{position:absolute;left:548px;top:2px;width:104px;height:104px;border-radius:50%;background:var(--brown);border:4px solid var(--amber);display:flex;align-items:center;justify-content:center;text-align:center;z-index:3;font-weight:600;font-size:12px;color:var(--amber);line-height:1.2}

/* hero */
.hero{position:absolute;left:0;top:67px;width:1200px;height:624px;overflow:hidden}
.hero h1{position:absolute;left:0;width:1200px;top:390px;text-align:center;color:var(--white);font-size:62px;line-height:54px;text-shadow:0 2px 8px rgba(0,0,0,.5)}
.arrow{position:absolute;stroke:var(--white);fill:none;stroke-width:2}

/* headings */
.section-title{font-family:'Bebas Neue',sans-serif;font-size:40px;line-height:40px;color:var(--ink)}
.body-copy{font-size:14px;line-height:27.5px;color:var(--text);text-align:justify}

/* features */
.tile{position:absolute;width:300px;height:238px}
.tile.text{background:var(--brown);color:var(--white);text-align:center;padding:60px 32px 0}
.tile h3{font-size:18px;font-weight:500;margin-bottom:14px}
.tile p{font-size:11px;line-height:23px;color:#e6ddd4}

/* reservation */
.card{position:absolute;left:125px;top:1785px;width:407px;height:374px;background:var(--amber)}
.field{position:absolute;left:35px;width:338px;height:46px;border-radius:23px;background:var(--white);font-size:14px;color:#777;display:flex;align-items:center;padding:0 20px;gap:10px}
.field .caret{margin-left:auto}

/* gallery */
.photo{position:absolute;border-radius:6px}

/* events */
.event{position:absolute;top:3889px;width:479px;height:249px;background:var(--white);box-shadow:0 4px 18px rgba(0,0,0,.12)}
.event .pic{position:absolute;left:0;top:0;width:240px;height:249px}
.event .date{position:absolute;left:202px;top:21px;width:49px;height:57px;background:var(--amber);color:var(--white);text-align:center;border:3px solid var(--white)}
.event .date b{display:block;font-family:'Bebas Neue',sans-serif;font-size:30px;line-height:30px;font-weight:400}
.event .date span{font-size:12px;line-height:14px}
.event h4{position:absolute;left:264px;top:28px;width:200px;font-size:16px;font-weight:500;line-height:24px}
.event p{position:absolute;left:264px;top:100px;width:200px;font-size:13px;line-height:27px;color:var(--text);text-align:justify}

/* footer */
.footer{position:absolute;left:0;top:4529px;width:1200px;height:365px;background:var(--footer);color:var(--white)}
.footer h5{position:absolute;font-size:14px;font-weight:500}
.footer ul{position:absolute;list-style:none;font-size:13px;line-height:29px}
.footer .info{position:absolute;font-size:13px;line-height:19px;display:flex;gap:12px;align-items:flex-start}
.social{position:absolute;top:4727px;width:38px;height:38px;border:1.5px solid var(--white);border-radius:50%}
</style>
</head>
<body>

<header class="nav">
  <a style="left:100px">FOOD MENU</a>
  <a style="left:249px">DRINKS MENU</a>
  <a style="left:410px">HAPPY HOUR</a>
  <a style="left:686px">CATERING</a>
  <a style="left:820px">SPECIAL EVENTS</a>
  <a style="left:999px">CONTACT US</a>
</header>
<div class="brand">Brennok<br>Sports Pub</div>

<section class="hero">
  <div class="media" role="img" aria-label="Crowd of fans cheering in front of screens at the pub" style="inset:0;background:
    radial-gradient(ellipse 220px 90px at 120px 60px,rgba(120,170,90,.85),rgba(120,170,90,0)),
    radial-gradient(ellipse 200px 80px at 820px 200px,rgba(110,160,90,.8),rgba(110,160,90,0)),
    radial-gradient(ellipse 180px 70px at 1100px 70px,rgba(120,170,90,.8),rgba(120,170,90,0)),
    radial-gradient(ellipse 260px 220px at 470px 260px,rgba(215,170,140,.55),rgba(215,170,140,0)),
    radial-gradient(ellipse 220px 200px at 180px 360px,rgba(200,160,130,.5),rgba(200,160,130,0)),
    radial-gradient(ellipse 240px 220px at 900px 380px,rgba(150,90,70,.55),rgba(150,90,70,0)),
    radial-gradient(ellipse 300px 160px at 600px 580px,rgba(70,60,80,.7),rgba(70,60,80,0)),
    linear-gradient(180deg,#3d3a2c 0%,#5a3a28 40%,#3a2720 75%,#221814 100%)"></div>
  <svg class="arrow" style="left:58px;top:298px" width="24" height="40"><polyline points="20,2 4,20 20,38"/></svg>
  <svg class="arrow" style="left:1118px;top:298px" width="24" height="40"><polyline points="4,2 20,20 4,38"/></svg>
  <h1 class="display">Brennok Sports Pub.<br>Where the locals go!!</h1>
  <div class="btn" style="left:427px;top:524px;width:167px;height:38px">Reservations</div>
  <div class="btn" style="left:608px;top:524px;width:165px;height:38px">Menu</div>
</section>

<section>
  <div class="sketch" role="img" aria-label="Line sketch of a beer glass" style="left:0;top:1020px;width:160px;height:220px"></div>
  <div class="sketch" role="img" aria-label="Line sketch of a cocktail glass" style="left:1060px;top:715px;width:140px;height:150px"></div>
  <div class="abs" style="left:133px;top:788px;width:17px;height:114px;background:var(--amber)"></div>
  <div class="abs" style="left:471px;top:1063px;width:131px;height:99px;background:var(--amber)"></div>
  <div class="media" role="img" aria-label="Pub bar counter with taps and screens" style="left:150px;top:756px;width:437px;height:389px;background:
    radial-gradient(ellipse 140px 50px at 90px 40px,rgba(150,180,210,.7),rgba(150,180,210,0)),
    radial-gradient(ellipse 120px 40px at 330px 60px,rgba(140,170,200,.6),rgba(140,170,200,0)),
    radial-gradient(ellipse 260px 90px at 230px 250px,rgba(220,140,60,.75),rgba(220,140,60,0)),
    radial-gradient(ellipse 220px 60px at 260px 330px,rgba(160,90,40,.8),rgba(160,90,40,0)),
    linear-gradient(180deg,#4c4038 0%,#6a4a30 45%,#8a5426 65%,#3a2418 100%)"></div>
  <h2 class="section-title abs" style="left:625px;top:776px">Welcome to<br>Brennok Sports Pub</h2>
  <div class="abs" style="left:968px;top:833px;width:132px;height:1px;background:#bbb"></div>
  <p class="body-copy abs" style="left:625px;top:870px;width:460px">Sed ut perspiciatis unde omnis iste natus error sit voluptatem accusantium doloremque laudantium, totam rem aperiam, eaque ipsa quae ab illo inventore veritatis et quasi architecto beatae vitae dicta sunt explicabo. Nemo enim ipsam voluptatem quia voluptas sit aspernatur aut odit aut fugit, sed quia consequuntur magni dolores eos qui ratione voluptatem sequi nesciunt. Neque porro quisquam</p>
  <div class="btn" style="left:625px;top:1085px;width:165px;height:38px">Learn more</div>
</section>

<section>
  <div class="tile text" style="left:0;top:1238px"><h3>TVS &amp; TECHNOLOGY</h3><p>Lorem ipsum dolor sit amet, consectetur adipiscing elit, sed do eiusmod tempor incididunt ut labore et dolore</p></div>
  <div class="tile media" role="img" aria-label="Busy pub interior with guests" style="left:300px;top:1238px;background:
    radial-gradient(ellipse 150px 60px at 150px 30px,rgba(230,80,50,.7),rgba(230,80,50,0)),
    radial-gradient(ellipse 120px 80px at 80px 170px,rgba(200,150,120,.5),rgba(200,150,120,0)),
    radial-gradient(ellipse 120px 80px at 230px 180px,rgba(180,130,110,.5),rgba(180,130,110,0)),
    linear-gradient(180deg,#7a2a1c 0%,#4a2418 50%,#2a1812 100%)"></div>
  <div class="tile text" style="left:600px;top:1238px"><h3>Fresh Food</h3><p>Lorem ipsum dolor sit amet, consectetur adipiscing elit, sed do eiusmod tempor incididunt ut labore et dolore</p></div>
  <div class="tile media" role="img" aria-label="Plates of fresh salad" style="left:900px;top:1238px;background:
    radial-gradient(ellipse 110px 60px at 160px 120px,rgba(230,190,70,.85),rgba(230,190,70,0)),
    radial-gradient(ellipse 90px 60px at 60px 90px,rgba(110,160,60,.8),rgba(110,160,60,0)),
    radial-gradient(ellipse 120px 50px at 150px 210px,rgba(240,240,240,.9),rgba(240,240,240,0)),
    linear-gradient(180deg,#7a6a5a 0%,#a89a80 50%,#d8d4cc 100%)"></div>
  <div class="tile media" role="img" aria-label="Row of craft beer glasses" style="left:0;top:1476px;background:
    radial-gradient(ellipse 40px 50px at 40px 130px,rgba(235,150,50,.95),rgba(235,150,50,0)),
    radial-gradient(ellipse 40px 50px at 110px 130px,rgba(60,30,20,.95),rgba(60,30,20,0)),
    radial-gradient(ellipse 40px 50px at 180px 130px,rgba(40,20,15,.95),rgba(40,20,15,0)),
    radial-gradient(ellipse 40px 50px at 250px 130px,rgba(225,150,60,.95),rgba(225,150,60,0)),
    linear-gradient(180deg,#4a4a4a 0%,#6a5a4a 40%,#9a6a3a 70%,#3a2a1a 100%)"></div>
  <div class="tile text" style="left:300px;top:1476px"><h3>Our Brew</h3><p>Lorem ipsum dolor sit amet, consectetur adipiscing elit, sed do eiusmod tempor incididunt ut labore et dolore</p></div>
  <div class="tile media" role="img" aria-label="Catering table set with glasses" style="left:600px;top:1476px;background:
    radial-gradient(ellipse 120px 70px at 210px 170px,rgba(240,215,150,.8),rgba(240,215,150,0)),
    radial-gradient(ellipse 100px 60px at 70px 190px,rgba(200,180,160,.8),rgba(200,180,160,0)),
    linear-gradient(180deg,#5a5048 0%,#bab2a6 45%,#e6e2da 100%)"></div>
  <div class="tile text" style="left:900px;top:1476px"><h3>Events &amp; catering Center</h3><p>Lorem ipsum dolor sit amet, consectetur adipiscing elit, sed do eiusmod tempor incididunt ut labore et dolore</p></div>
</section>

<section>
  <div class="card">
    <div class="display abs" style="left:0;width:407px;top:30px;text-align:center;font-size:38px;color:var(--white)">Find Table</div>
    <div class="field" style="top:95px">▦ Date <span class="caret">▾</span></div>
    <div class="field" style="top:159px">◷ Time <span class="caret">▾</span></div>
    <div class="field" style="top:222px">● Person <span class="caret">▾</span></div>
    <div class="btn" style="left:35px;top:287px;width:338px;height:46px;background:var(--brown-deep);border-radius:23px;font-size:14px">Reserve now</div>
  </div>
  <h2 class="section-title abs" style="left:600px;top:1793px">Reservation at<br>Brennok Sports Pub</h2>
  <div class="abs" style="left:940px;top:1850px;width:135px;height:1px;background:var(--amber-light)"></div>
  <p class="body-copy abs" style="left:600px;top:1890px;width:458px">Sed ut perspiciatis unde omnis iste natus error sit voluptatem accusantium doloremque laudantium, totam rem aperiam, eaque ipsa quae ab illo inventore veritatis et quasi architecto beatae vitae dicta sunt explicabo. Nemo enim ipsam voluptatem quia voluptas sit aspernatur aut odit aut fugit, sed quia consequuntur magni dolores</p
  ><p class="abs" style="left:600px;top:2066px;width:420px;font-size:14px;line-height:28px;font-style:italic;color:#555">We Kindly ask you to contact us personally for table reservations from 6 persons</p>
  <p class="abs" style="left:600px;top:2131px;font-size:14px;color:#333">Call : 123 456 7890</p>
  <div class="sketch" role="img" aria-label="Line sketch of a wine bottle and corkscrew" style="left:1045px;top:2040px;width:145px;height:185px"></div>
</section>

<section class="abs" style="left:0;top:2231px;width:1200px;height:437px">
  <div class="media" role="img" aria-label="Dim bar with shelves of bottles" style="inset:0;background:
    radial-gradient(ellipse 300px 120px at 1000px 110px,rgba(120,110,90,.45),rgba(120,110,90,0)),
    radial-gradient(ellipse 240px 110px at 200px 120px,rgba(90,100,100,.45),rgba(90,100,100,0)),
    radial-gradient(ellipse 500px 90px at 600px 390px,rgba(110,70,40,.6),rgba(110,70,40,0)),
    linear-gradient(180deg,#2a3236 0%,#1f2224 45%,#1c1a18 70%,#2e2016 100%)"></div>
  <div class="display abs" style="left:0;width:1200px;top:115px;text-align:center;color:var(--white);font-size:40px">Private Events</div>
  <p class="abs" style="left:225px;width:750px;top:170px;text-align:center;color:var(--white);font-size:14px;line-height:31px">Sed ut perspiciatis unde omnis iste natus error sit voluptatem accusantium doloremque laudantium, totam rem aperiam, eaque ipsa quae ab illo inventore veritatis et quasi architecto beatae vitae dicta sunt explicabo. Nemo enim ipsam voluptatem</p>
  <div class="btn" style="left:517px;top:277px;width:165px;height:38px">Inquire</div>
</section>

<section>
  <h2 class="section-title abs" style="left:0;width:1200px;top:2728px;text-align:center">Our Gallery</h2>
  <div class="sketch" role="img" aria-label="Line sketch of a beer glass" style="left:0;top:3120px;width:150px;height:210px"></div>
  <div class="photo" role="img" aria-label="Guests reading menus at a table" style="left:99px;top:2799px;width:364px;height:444px;background:
    radial-gradient(ellipse 60px 30px at 200px 90px,rgba(170,200,220,.7),rgba(170,200,220,0)),
    radial-gradient(ellipse 120px 90px at 80px 320px,rgba(190,140,110,.6),rgba(190,140,110,0)),
    radial-gradient(ellipse 110px 60px at 200px 380px,rgba(220,210,190,.7),rgba(220,210,190,0)),
    linear-gradient(180deg,#5a4634 0%,#3e3026 50%,#2a221c 100%)"></div>
  <div class="photo" role="img" aria-label="Bar counter with screens" style="left:477px;top:2799px;width:260px;height:174px;background:
    radial-gradient(ellipse 70px 30px at 50px 20px,rgba(110,170,90,.8),rgba(110,170,90,0)),
    radial-gradient(ellipse 70px 30px at 210px 20px,rgba(110,170,90,.8),rgba(110,170,90,0)),
    radial-gradient(ellipse 120px 40px at 130px 150px,rgba(160,100,50,.7),rgba(160,100,50,0)),
    linear-gradient(180deg,#4a5a44 0%,#2e2620 45%,#241c16 100%)"></div>
  <div class="photo" role="img" aria-label="Shelves of bottles behind the bar" style="left:477px;top:2989px;width:260px;height:252px;background:
    radial-gradient(ellipse 90px 50px at 60px 40px,rgba(200,80,50,.6),rgba(200,80,50,0)),
    radial-gradient(ellipse 80px 100px at 200px 110px,rgba(90,110,110,.6),rgba(90,110,110,0)),
    linear-gradient(180deg,#6a3a24 0%,#4a3226 50%,#2a221e 100%)"></div>
  <div class="photo" role="img" aria-label="Long bar with hanging lights" style="left:750px;top:2799px;width:350px;height:264px;background:
    radial-gradient(ellipse 140px 50px at 175px 110px,rgba(150,190,210,.45),rgba(150,190,210,0)),
    radial-gradient(ellipse 180px 50px at 175px 230px,rgba(200,120,50,.75),rgba(200,120,50,0)),
    linear-gradient(180deg,#222a30 0%,#2e3a40 45%,#3a2a1e 80%,#5a3a22 100%)"></div>
  <div class="photo" role="img" aria-label="Drinks being served" style="left:750px;top:3080px;width:169px;height:161px;background:
    radial-gradient(ellipse 50px 40px at 110px 110px,rgba(200,160,130,.6),rgba(200,160,130,0)),
    radial-gradient(ellipse 40px 30px at 50px 60px,rgba(180,140,120,.5),rgba(180,140,120,0)),
    linear-gradient(160deg,#3a3434 0%,#221c1c 100%)"></div>
  <div class="photo" role="img" aria-label="Glasses of whiskey on a table" style="left:933px;top:3080px;width:169px;height:161px;background:
    radial-gradient(ellipse 60px 30px at 90px 130px,rgba(220,140,50,.9),rgba(220,140,50,0)),
    radial-gradient(ellipse 50px 40px at 50px 60px,rgba(160,110,80,.6),rgba(160,110,80,0)),
    linear-gradient(180deg,#7a8a94 0%,#8a7a6a 50%,#6a4a2e 100%)"></div>
</section>

<section class="abs" style="left:0;top:3319px;width:1200px;height:437px;background:var(--amber);color:var(--white)">
  <div class="display abs" style="left:0;width:1200px;top:80px;text-align:center;font-size:40px">What people are saying!</div>
  <div class="abs" style="left:0;width:1200px;top:160px;text-align:center;font-size:18px;letter-spacing:3px">★★★★★</div>
  <p class="abs" style="left:225px;width:750px;top:193px;text-align:center;font-size:15px;line-height:32px;font-style:italic">Lorem ipsum dolor sit amet, consectetur adipiscing elit, sed do eiusmod tempor incididunt ut labore et dolore magna aliqua. Quis ipsum suspendisse ultrices gravida. Risus commodo viverra maecenas accumsan lacus vel facilisis.</p>
  <svg class="arrow" style="left:128px;top:222px" width="40" height="16"><polyline points="8,2 2,8 8,14"/><line x1="2" y1="8" x2="38" y2="8"/></svg>
  <svg class="arrow" style="left:1025px;top:222px" width="40" height="16"><polyline points="32,2 38,8 32,14"/><line x1="2" y1="8" x2="38" y2="8"/></svg>
  <div class="abs" role="img" aria-label="Reviewer portrait" style="left:520px;top:311px;width:44px;height:44px;border-radius:50%;background:radial-gradient(circle at 50% 40%,#d8b494,#8a6a4e)"></div>
  <div class="abs" style="left:577px;top:321px;font-size:17px;font-weight:500">Dana Morrow</div>
</section>

<section>
  <h2 class="section-title abs" style="left:0;width:1200px;top:3818px;text-align:center">Lastest Events</h2>
  <div class="sketch" role="img" aria-label="Line sketch of a cocktail glass" style="left:1080px;top:3800px;width:120px;height:140px"></div>
  <article class="event" style="left:106px">
    <div class="pic" role="img" aria-label="DJ hands on mixing deck" style="background:
      radial-gradient(ellipse 90px 60px at 140px 90px,rgba(170,110,200,.7),rgba(170,110,200,0)),
      radial-gradient(ellipse 100px 30px at 120px 200px,rgba(220,60,60,.55),rgba(220,60,60,0)),
      radial-gradient(ellipse 80px 40px at 60px 40px,rgba(60,90,200,.7),rgba(60,90,200,0)),
      linear-gradient(180deg,#1a2450 0%,#241838 55%,#0c0c16 100%)"></div>
    <div class="date"><b>10</b><span>JUL</span></div>
    <h4>The standard Lorem Ips um passage, used</h4>
    <p>Sed ut perspicia de omnis isr sit volupm accusantium doloremque lantium, totam rem aperiam, eaque ipsa quae ab illo</p>
    <svg class="arrow" style="left:443px;top:220px;stroke:#555" width="22" height="12"><line x1="1" y1="6" x2="20" y2="6"/><polyline points="15,1 20,6 15,11"/></svg>
  </article>
  <article class="event" style="left:617px">
    <div class="pic" role="img" aria-label="Chef plating food" style="background:
      radial-gradient(ellipse 80px 60px at 120px 60px,rgba(240,230,215,.85),rgba(240,230,215,0)),
      radial-gradient(ellipse 90px 50px at 120px 190px,rgba(200,120,60,.7),rgba(200,120,60,0)),
      linear-gradient(180deg,#c8bca8 0%,#9a7a5a 55%,#5a3e26 100%)"></div>
    <div class="date"><b>10</b><span>JUL</span></div>
    <h4>The standard Lorem Ips um passage, used</h4>
    <p>Sed ut perspicia de omnis isr sit volupm accusantium doloremque lantium, totam rem aperiam, eaque ipsa quae ab illo</p>
    <svg class="arrow" style="left:443px;top:220px;stroke:#555" width="22" height="12"><line x1="1" y1="6" x2="20" y2="6"/><polyline points="15,1 20,6 15,11"/></svg>
  </article>
</section>

<section class="abs" style="left:0;top:4215px;width:1200px;height:314px">
  <div class="media" role="img" aria-label="Fans celebrating at the bar" style="inset:0;background:
    radial-gradient(ellipse 160px 140px at 840px 160px,rgba(170,110,70,.6),rgba(170,110,70,0)),
    radial-gradient(ellipse 140px 130px at 1080px 150px,rgba(150,100,70,.55),rgba(150,100,70,0)),
    radial-gradient(ellipse 120px 80px at 950px 40px,rgba(220,170,100,.4),rgba(220,170,100,0)),
    linear-gradient(90deg,#1a1614 0%,#1e1814 45%,#3a2a20 75%,#2a1e18 100%)"></div>
  <div class="display abs" style="left:103px;top:80px;font-size:40px;color:var(--white)">Join our mobile VIP club</div>
  <p class="abs" style="left:103px;top:133px;font-size:13px;font-style:italic;color:var(--white)">Receive freebies, discounts and club member only specials.</p>
  <div class="abs" style="left:103px;top:183px;width:560px;height:42px;border-radius:21px;background:var(--white);font-size:13px;color:#333;padding:11px 28px">Enter Your Email Addresss</div>
  <div class="btn" style="left:494px;top:183px;width:169px;height:42px;border-radius:21px;font-size:14px">Subscribe now</div>
</section>

<footer class="footer">
  <div class="abs" style="left:114px;top:50px;width:224px;height:224px;border-radius:50%;background:var(--brown);border:6px solid var(--amber);display:flex;align-items:center;justify-content:center;text-align:center;font-size:22px;font-weight:600;color:var(--amber);line-height:1.3">Brennok<br>Sports Pub</div>
  <h5 style="left:422px;top:58px">QUICK LINKS</h5>
  <ul style="left:422px;top:84px"><li>Home</li><li>Food Menu</li><li>Drinks Menu</li><li>Happy Hour</li><li>Catering</li><li>Special Events</li><li>Contact Us</li></ul>
  <h5 style="left:600px;top:58px">CONTACT INFO</h5>
  <div class="info" style="left:600px;top:96px"><svg width="30" height="30"><circle cx="15" cy="15" r="14" fill="none" stroke="#fff" stroke-width="1.5"/><path d="M15 8a5 5 0 0 1 5 5c0 4-5 9-5 9s-5-5-5-9a5 5 0 0 1 5-5z" fill="none" stroke="#fff" stroke-width="1.5"/></svg><span>1234 Main Rd<br>Somewhere, US 12345</span></div>
  <div class="info" style="left:600px;top:155px"><svg width="30" height="30"><circle cx="15" cy="15" r="14" fill="none" stroke="#fff" stroke-width="1.5"/><path d="M10 9l3 0 1 4-2 1c1 2 2 3 4 4l1-2 4 1 0 3c-7 0-11-4-11-11z" fill="none" stroke="#fff" stroke-width="1.3"/></svg><span style="padding-top:6px">+1 888 888 8888</span></div>
  <div class="info" style="left:600px;top:208px"><svg width="30" height="30"><circle cx="15" cy="15" r="14" fill="none" stroke="#fff" stroke-width="1.5"/><rect x="8" y="10" width="14" height="10" fill="none" stroke="#fff" stroke-width="1.3"/><polyline points="8,10 15,16 22,10" fill="none" stroke="#fff" stroke-width="1.3"/></svg><span style="padding-top:6px">info@BrennokSportsPub.com</span></div>
  <h5 style="left:923px;top:58px">OPENING HOURS</h5>
  <ul style="left:923px;top:84px"><li>Week Days: 09:00 to 18:00</li><li>Saturday: 09:00 to 13:00</li><li>Sunday: 09:00 to 13:00</li></ul>
  <p class="abs" style="left:0;width:1200px;top:322px;text-align:center;font-size:12px">©Copyright 2023 Brennok Sports Pub. All Rights Reserved.</p>
</footer>
<div class="social" style="left:920px"></div>
<div class="social" style="left:968px"></div>
<div class="social" style="left:1015px"></div>
<div class="social" style="left:1061px"></div>

</body>
</html>
```